VOXterra Roadmap for developing engineer 3D-BIM-projects over a longer period of time

We need functional and scalable PowerPoint templates with four main slides. The design should be carried out in the context of the enclosed documents; or at least in this sense.
As engineers, we develop projects over a longer period of time. To visualize topics along the way (downside timeline) and goals (upside timeline) for our customers (and for us), we need an overview for the project management in sort of a roadmap.
Our design requirements are simplicity, clarity and accuracy. These are also the service requirements for our customers.
As always, it's urgent. Our goal is to select the design by Wednesday November 10th and make any adjustments with the winner by Friday November 12th.

Target Market(s)

Architects, Engineers, World Heritage; 3D-Modelling, BIM Building Information Modeling

Industry/Entity Type

World Heritage Buildings and Objects

Requirements
Must have
• simplicity, logic, elegant (see the attached documents)
Nice to have
• see the attached documents

```html
<!DOCTYPE html>
<html lang="de">
<head>
<meta charset="utf-8">
<title>VOXterra Roadmap Templates</title>
<link rel="stylesheet" href="https://fonts.googleapis.com/css2?family=Roboto:wght@300;400;500;700&family=Montserrat:wght@800&display=swap">
<style>
:root{
  --stage:#c8c8c8;
  --paper:#ffffff;
  --ink:#111111;
  --muted:#555555;
  --rail:#7a7a7a;
  --band:#efefef;
  --hair:#c9c9c9;
  --gold:#c9a449;
  --accent:#e2331b;
  --brand-blue:#1463ad;
}
*{margin:0;padding:0;box-sizing:border-box}
html,body{width:797px;height:1200px;overflow:hidden;background:var(--stage)}
body{position:relative;font-family:"Roboto",Arial,sans-serif;color:var(--ink)}
.slide{position:absolute;width:345px;height:259px;background:var(--paper);overflow:hidden}
.col-a{left:44px}.col-b{left:408px}
.row-1{top:55px}.row-2{top:331px}.row-3{top:608px}.row-4{top:885px}
.slide svg.layer{position:absolute;left:0;top:0;width:345px;height:259px}
.slide-title{position:absolute;left:21px;font-size:13px;font-weight:700;line-height:1}
.slide-year{position:absolute;right:20px;font-size:13px;font-weight:300;line-height:1}
.brand-mark{position:absolute;left:22px;top:244px;width:7px;height:7px;background:var(--accent)}
.wordmark{position:absolute;left:0;right:0;top:80px;display:flex;justify-content:center;align-items:center;gap:6px}
.wordmark .dot{width:10px;height:10px;background:var(--accent)}
.wordmark .name{font-size:28px;font-weight:700;color:var(--brand-blue);letter-spacing:-.5px;line-height:1}
.cover-rule{position:absolute;left:38px;width:268px;top:124px;border-top:1px solid var(--gold)}
.cover-title{position:absolute;left:0;right:0;top:139px;text-align:center;font-size:16.5px;font-weight:500}
.cover-hair{position:absolute;left:87px;width:169px;border-top:1px solid var(--hair)}
.cover-sub{position:absolute;left:0;right:0;top:168px;text-align:center;font-size:5.8px;line-height:9px;color:var(--muted)}
.topic-title{position:absolute;left:56px;width:232px;text-align:center;font-size:8.5px;font-weight:700}
.topic-rule{position:absolute;left:56px;width:232px;border-top:1px solid var(--gold)}
.topic-box{position:absolute;left:56px;width:232px;height:97px;background:var(--band);padding:14px 15px 0 15px}
.topic-box p{font-size:5.8px;line-height:9px;color:#444;margin-bottom:7.4px}
.topic-box ul{list-style:none;padding-left:2px}
.topic-box li{font-size:5.8px;line-height:6px;color:#222;margin-bottom:8.9px;position:relative;padding-left:9px}
.topic-box li::before{content:"";position:absolute;left:0;top:1.2px;width:3.4px;height:3.4px;border-radius:50%;background:#111}
.switch-label{position:absolute;left:289px;top:146px;width:218px;display:flex;align-items:center;gap:5px;z-index:2}
.switch-label span{font-family:"Montserrat",Arial,sans-serif;font-weight:800;font-size:15px;letter-spacing:.6px}
.switch-label i{flex:1;border-top:1.2px solid var(--ink)}
svg text{font-family:"Roboto",Arial,sans-serif}
.m{font-size:5.4px;font-weight:700;text-anchor:middle;fill:var(--ink)}
.ms{font-size:5.6px;text-anchor:middle;fill:var(--ink)}
.row{font-size:5.2px;text-anchor:middle;fill:#222}
</style>
</head>
<body>

<div class="switch-label"><i></i><span>SWITCHING</span><i></i></div>

<!-- Cover slides -->
<section class="slide col-a row-1">
  <div class="wordmark"><div class="dot"></div><div class="name">VOXterra</div></div>
  <div class="cover-rule"></div>
  <h1 class="cover-title">Projectname</h1>
  <div class="cover-hair" style="top:165px"></div>
  <p class="cover-sub">Maecenas sed diam dget risusu ipsum dolor sit amet, consectetur adipiscing elit ds.<br>Nam suscipit felis sit amet nib Nam suscipit felis sit</p>
  <div class="cover-hair" style="top:190px"></div>
</section>
<section class="slide col-b row-1">
  <div class="wordmark"><div class="dot"></div><div class="name">NOVAterra</div></div>
  <div class="cover-rule"></div>
  <h1 class="cover-title">Projectname</h1>
  <div class="cover-hair" style="top:165px"></div>
  <p class="cover-sub">Maecenas sed diam dget risusu ipsum dolor sit amet, consectetur adipiscing elit ds.<br>Nam suscipit felis sit amet nib Nam suscipit felis sit</p>
  <div class="cover-hair" style="top:190px"></div>
</section>

<!-- Overview slides -->
<section class="slide col-a row-2">
  <h2 class="slide-title" style="top:20px">Roadmap</h2>
  <div class="slide-year" style="top:20px">2021</div>
  <svg class="layer" viewBox="0 0 345 259">
    <g stroke="var(--ink)" stroke-width=".8">
      <line x1="123.5" y1="129" x2="123.5" y2="111"/><line x1="163" y1="129" x2="163" y2="97"/>
      <line x1="262" y1="129" x2="262" y2="79"/><line x1="283.5" y1="129" x2="283.5" y2="63"/>
    </g>
    <g fill="var(--ink)"><circle cx="123.5" cy="111" r="1.3"/><circle cx="163" cy="97" r="1.3"/><circle cx="262" cy="79" r="1.3"/><circle cx="283.5" cy="63" r="1.3"/></g>
    <text class="ms" x="123.5" y="106">Kick-off</text><text class="ms" x="163" y="92">Datenbanken</text>
    <text class="ms" x="262" y="74">Mock-up</text><text class="ms" x="282" y="58">Roadmap 2022</text>
    <g transform="translate(0,129)">
      <line x1="24" y1="0" x2="320" y2="0" stroke="var(--rail)" stroke-width="1.5"/>
      <path d="M28 -8 L21 0 L28 8 M314 -8 L321 0 L314 8" fill="none" stroke="var(--rail)" stroke-width="1.3"/>
      <path d="M44 -5 L50 0 L44 5" fill="none" stroke="var(--accent)" stroke-width="1"/>
      <g fill="var(--ink)"><circle cx="63.5" cy="0" r="2.7"/><circle cx="104" cy="0" r="2.7"/><circle cx="223" cy="0" r="2.7"/></g>
      <g fill="#fff" stroke="var(--ink)" stroke-width="1"><circle cx="123.5" r="5"/><circle cx="163" r="5"/><circle cx="262" r="5"/><circle cx="283.5" r="5"/></g>
      <g fill="var(--ink)"><circle cx="123.5" r="2.3"/><circle cx="163" r="2.3"/><circle cx="262" r="2.3"/><circle cx="283.5" r="2.3"/></g>
      <text class="m" x="62.5" y="13">JAN</text><text class="m" x="104" y="13">MAR</text><text class="m" x="123.5" y="13">APR</text><text class="m" x="162" y="13">JUN</text><text class="m" x="223" y="13">SEP</text><text class="m" x="262" y="13">NOV</text><text class="m" x="283" y="13">DEZ</text>
    </g>
    <g fill="var(--band)"><rect x="20" y="153" width="303.5" height="14.7"/><rect x="20" y="182.4" width="303.5" height="14.7"/><rect x="20" y="211.8" width="303.5" height="14.7"/></g>
    <g stroke="#333" stroke-width=".5">
      <line x1="49" y1="166" x2="94.5" y2="166"/><line x1="66" y1="180.8" x2="94" y2="180.8"/>
      <line x1="94" y1="195.4" x2="272" y2="195.4"/><line x1="126" y1="210.2" x2="253" y2="210.2"/>
      <line x1="210" y1="224.9" x2="250" y2="224.9"/><line x1="272" y1="239.6" x2="323" y2="239.6"/>
    </g>
    <text class="row" x="72" y="163">Laserscanning</text><text class="row" x="80" y="177.8">Drohne</text>
    <text class="row" x="183" y="192.4">Datenprozessierung</text><text class="row" x="189.5" y="207.2">Datenbankmanagementsystem</text>
    <text class="row" x="230" y="221.9">3D-Modellierung</text><text class="row" x="297.5" y="236.6">BIM-Viewer</text>
  </svg>
  <div class="brand-mark"></div>
</section>

<section class="slide col-b row-2">
  <h2 class="slide-title" style="top:20px">Roadmap</h2>
  <div class="slide-year" style="top:20px">2021</div>
  <svg class="layer" viewBox="0 0 345 259">
    <g stroke="var(--ink)" stroke-width=".8">
      <line x1="123.5" y1="129" x2="123.5" y2="115"/><line x1="163" y1="129" x2="163" y2="105"/>
      <line x1="262" y1="129" x2="262" y2="92"/><line x1="283.5" y1="129" x2="283.5" y2="70"/>
    </g>
    <g fill="var(--ink)"><circle cx="123.5" cy="115" r="1.3"/><circle cx="163" cy="105" r="1.3"/><circle cx="262" cy="92" r="1.3"/><circle cx="283.5" cy="70" r="1.3"/></g>
    <text class="ms" x="123.5" y="110.5">Kick-off</text><text class="ms" x="163" y="99.5">Datenbanken</text>
    <text class="ms" x="262" y="88">Mock-up</text><text class="ms" x="285" y="66">Roadmap 2022</text>
    <g fill="none" stroke="#888" stroke-width=".5">
      <path d="M121 102 L128 93 L129.5 94.5 L122.5 103 Z M121 102 L119 101 M122.5 103 L123 105"/>
      <ellipse cx="163" cy="84" rx="4" ry="1.5"/><path d="M159 84 V91 M167 84 V91 M159 87.5 Q163 89.5 167 87.5 M159 91 Q163 93 167 91"/>
      <path d="M262 71 L266 73 L266 77.5 L262 79.5 L258 77.5 L258 73 Z M258 73 L262 75 L266 73 M262 75 V79.5"/>
      <path d="M280 51 V59 M280 51 H285 L284 53 L285 55 H280 M281 58 H290 Q291 60 289 60 H284"/>
    </g>
    <g transform="translate(0,129)">
      <line x1="24" y1="0" x2="320" y2="0" stroke="var(--rail)" stroke-width="1.5"/>
      <path d="M28 -8 L21 0 L28 8 M314 -8 L321 0 L314 8" fill="none" stroke="var(--rail)" stroke-width="1.3"/>
      <path d="M44 -5 L50 0 L44 5" fill="none" stroke="var(--accent)" stroke-width="1"/>
      <g fill="var(--ink)"><circle cx="63.5" cy="0" r="2.7"/><circle cx="104" cy="0" r="2.7"/><circle cx="223" cy="0" r="2.7"/></g>
      <g fill="#fff" stroke="var(--ink)" stroke-width="1"><circle cx="123.5" r="5"/><circle cx="163" r="5"/><circle cx="262" r="5"/><circle cx="283.5" r="5"/></g>
      <g fill="var(--ink)"><circle cx="123.5" r="2.3"/><circle cx="163" r="2.3"/><circle cx="262" r="2.3"/><circle cx="283.5" r="2.3"/></g>
      <text class="m" x="62.5" y="13">JAN</text><text class="m" x="104" y="13">MAR</text><text class="m" x="123.5" y="13">APR</text><text class="m" x="162" y="13">JUN</text><text class="m" x="223" y="13">SEP</text><text class="m" x="262" y="13">NOV</text><text class="m" x="283" y="13">DEZ</text>
    </g>
    <g fill="var(--band)"><rect x="20" y="153" width="303.5" height="14.7"/><rect x="20" y="182.4" width="303.5" height="14.7"/><rect x="20" y="211.8" width="303.5" height="14.7"/></g>
    <g stroke="#333" stroke-width=".5">
      <line x1="49" y1="166" x2="94.5" y2="166"/><line x1="66" y1="180.8" x2="94" y2="180.8"/>
      <line x1="94" y1="195.4" x2="272" y2="195.4"/><line x1="126" y1="210.2" x2="253" y2="210.2"/>
      <line x1="210" y1="224.9" x2="250" y2="224.9"/><line x1="272" y1="239.6" x2="323" y2="239.6"/>
    </g>
    <text class="row" x="72" y="163">Laserscanning</text><text class="row" x="80" y="177.8">Drohne</text>
    <text class="row" x="183" y="192.4">Datenprozessierung</text><text class="row" x="189.5" y="207.2">Datenbankmanagementsystem</text>
    <text class="row" x="230" y="221.9">3D-Modellierung</text><text class="row" x="297.5" y="236.6">BIM-Viewer</text>
  </svg>
  <div class="brand-mark"></div>
</section>

<!-- Topic slides (downside) -->
<section class="slide col-a row-3">
  <h2 class="slide-title" style="top:20px">Roadmap</h2>
  <div class="slide-year" style="top:20px">2021</div>
  <svg class="layer" viewBox="0 0 345 259">
    <g transform="translate(0,73)">
      <line x1="24" y1="0" x2="320" y2="0" stroke="var(--rail)" stroke-width="1.5"/>
      <line x1="53" y1="0" x2="94.5" y2="0" stroke="var(--accent)" stroke-width="1.8"/>
      <path d="M28 -8 L21 0 L28 8 M314 -8 L321 0 L314 8" fill="none" stroke="var(--rail)" stroke-width="1.3"/>
      <path d="M44 -5 L50 0 L44 5" fill="none" stroke="var(--ink)" stroke-width="1"/>
      <g fill="var(--ink)"><circle cx="63.5" cy="0" r="2.7"/><circle cx="104" cy="0" r="2.7"/><circle cx="223" cy="0" r="2.7"/></g>
      <g fill="#fff" stroke="var(--ink)" stroke-width="1"><circle cx="123.5" r="5"/><circle cx="163" r="5"/><circle cx="262" r="5"/><circle cx="283.5" r="5"/></g>
      <g fill="var(--ink)"><circle cx="123.5" r="2.3"/><circle cx="163" r="2.3"/><circle cx="262" r="2.3"/><circle cx="283.5" r="2.3"/></g>
      <text class="m" x="62.5" y="13">JAN</text><text class="m" x="104" y="13">MAR</text><text class="m" x="123.5" y="13">APR</text><text class="m" x="162" y="13">JUN</text><text class="m" x="223" y="13">SEP</text><text class="m" x="262" y="13">NOV</text><text class="m" x="283" y="13">DEZ</text>
    </g>
    <path d="M163 133 L172 137 L181 133" fill="none" stroke="#555" stroke-width=".5"/>
  </svg>
  <h3 class="topic-title" style="top:111px">Laserscanning</h3>
  <div class="topic-rule" style="top:125px"></div>
  <div class="topic-box" style="top:142px">
    <p>Maecenas sed diam dget risusu ipsum dolor sit amet, consectetur adipiscing elit ds. Nam suscipit felis sit amet nib Nam suscipit felis sit Maecenas sed</p>
    <p>Maecenas sed diam dget risusu ipsum dolor sit amet, consectetur adipiscing elit ds. Nam suscipit felis sit amet nib Nam suscipit felis sit Maecenas sed</p>
    <p>Maecenas sed diam dget risusu ipsum dolor sit amet, consectetur adipiscing elit ds. Nam suscipit felis sit amet nib Nam suscipit felis sit Maecenas sed</p>
  </div>
  <div class="brand-mark"></div>
</section>

<section class="slide col-b row-3">
  <h2 class="slide-title" style="top:20px">Roadmap</h2>
  <div class="slide-year" style="top:20px">2021</div>
  <svg class="layer" viewBox="0 0 345 259">
    <g transform="translate(0,73)">
      <line x1="24" y1="0" x2="320" y2="0" stroke="var(--rail)" stroke-width="1.5"/>
      <line x1="53" y1="0" x2="94.5" y2="0" stroke="var(--accent)" stroke-width="1.8"/>
      <path d="M28 -8 L21 0 L28 8 M314 -8 L321 0 L314 8" fill="none" stroke="var(--rail)" stroke-width="1.3"/>
      <path d="M44 -5 L50 0 L44 5" fill="none" stroke="var(--ink)" stroke-width="1"/>
      <g fill="var(--ink)"><circle cx="63.5" cy="0" r="2.7"/><circle cx="104" cy="0" r="2.7"/><circle cx="223" cy="0" r="2.7"/></g>
      <g fill="#fff" stroke="var(--ink)" stroke-width="1"><circle cx="123.5" r="5"/><circle cx="163" r="5"/><circle cx="262" r="5"/><circle cx="283.5" r="5"/></g>
      <g fill="var(--ink)"><circle cx="123.5" r="2.3"/><circle cx="163" r="2.3"/><circle cx="262" r="2.3"/><circle cx="283.5" r="2.3"/></g>
      <text class="m" x="62.5" y="13">JAN</text><text class="m" x="104" y="13">MAR</text><text class="m" x="123.5" y="13">APR</text><text class="m" x="162" y="13">JUN</text><text class="m" x="223" y="13">SEP</text><text class="m" x="262" y="13">NOV</text><text class="m" x="283" y="13">DEZ</text>
    </g>
    <path d="M163 133 L172 137 L181 133" fill="none" stroke="#555" stroke-width=".5"/>
  </svg>
  <h3 class="topic-title" style="top:111px">Laserscanning</h3>
  <div class="topic-rule" style="top:125px"></div>
  <div class="topic-box" style="top:142px;padding-top:16px">
    <ul>
      <li>Maecenas sed diam dget risusu ipsum dolor sit amet, consectetur nsec</li>
      <li>Maecenas sed diam dget risusu ipsum dolor sit amet, consectetur nsec</li>
      <li>Maecenas sed diam dget risusu ipsum dolor sit amet, consectetur nsec</li>
      <li>Maecenas sed diam dget risusu ipsum dolor sit amet, consectetur nsec</li>
      <li>Maecenas sed diam dget risusu ipsum dolor sit amet, consectetur nsec</li>
    </ul>
  </div>
  <div class="brand-mark"></div>
</section>

<!-- Goal slides (upside) -->
<section class="slide col-a row-4">
  <div class="topic-box" style="top:20px">
    <p style="color:#222">Maecenas sed diam dget risusu ipsum dolor sit amet, consectetur adipiscing elit ds. Nam suscipit felis sit amet nib Nam suscipit felis sit Maecenas sed</p>
    <p style="color:#222">Maecenas sed diam dget risusu ipsum dolor sit amet, consectetur adipiscing elit ds. Nam suscipit felis sit amet nib Nam suscipit felis sit Maecenas sed</p>
    <p style="color:#222">Maecenas sed diam dget risusu ipsum dolor sit amet, consectetur adipiscing elit ds. Nam suscipit felis sit amet nib Nam suscipit felis sit Maecenas sed</p>
  </div>
  <svg class="layer" viewBox="0 0 345 259">
    <path d="M163 131 L172 127 L181 131" fill="none" stroke="#555" stroke-width=".5"/>
    <g transform="translate(0,186.5)">
      <line x1="24" y1="0" x2="320" y2="0" stroke="var(--rail)" stroke-width="1.5"/>
      <path d="M28 -8 L21 0 L28 8 M314 -8 L321 0 L314 8" fill="none" stroke="var(--rail)" stroke-width="1.3"/>
      <path d="M44 -5 L50 0 L44 5" fill="none" stroke="var(--ink)" stroke-width="1"/>
      <g fill="var(--ink)"><circle cx="63.5" cy="0" r="2.7"/><circle cx="104" cy="0" r="2.7"/><circle cx="223" cy="0" r="2.7"/></g>
      <g fill="#fff" stroke="var(--ink)" stroke-width="1"><circle cx="163" r="5"/><circle cx="262" r="5"/><circle cx="283.5" r="5"/></g>
      <circle cx="123.5" r="5" fill="#fff" stroke="var(--accent)" stroke-width="1"/>
      <g fill="var(--ink)"><circle cx="163" r="2.3"/><circle cx="262" r="2.3"/><circle cx="283.5" r="2.3"/></g>
      <circle cx="123.5" r="2.3" fill="var(--accent)"/>
      <text class="m" x="62.5" y="13">JAN</text><text class="m" x="104" y="13">MAR</text><text class="m" x="123.5" y="13">APR</text><text class="m" x="162" y="13">JUN</text><text class="m" x="223" y="13">SEP</text><text class="m" x="262" y="13">NOV</text><text class="m" x="283" y="13">DEZ</text>
    </g>
  </svg>
  <div class="topic-rule" style="top:140px"></div>
  <h3 class="topic-title" style="top:145px">Kick-off</h3>
  <h2 class="slide-title" style="top:225px;left:20px">Roadmap</h2>
  <div class="slide-year" style="top:228px">2021</div>
  <div class="brand-mark"></div>
</section>

<section class="slide col-b row-4">
  <div class="topic-box" style="top:20px;padding-top:16px">
    <ul>
      <li>Maecenas sed diam dget risusu ipsum dolor sit amet, consectetur nsec</li>
      <li>Maecenas sed diam dget risusu ipsum dolor sit amet, consectetur nsec</li>
      <li>Maecenas sed diam dget risusu ipsum dolor sit amet, consectetur nsec</li>
      <li>Maecenas sed diam dget risusu ipsum dolor sit amet, consectetur nsec</li>
      <li>Maecenas sed diam dget risusu ipsum dolor sit amet, consectetur nsec</li>
    </ul>
  </div>
  <svg class="layer" viewBox="0 0 345 259">
    <path d="M163 131 L172 127 L181 131" fill="none" stroke="#555" stroke-width=".5"/>
    <g transform="translate(0,186.5)">
      <line x1="24" y1="0" x2="320" y2="0" stroke="var(--rail)" stroke-width="1.5"/>
      <path d="M28 -8 L21 0 L28 8 M314 -8 L321 0 L314 8" fill="none" stroke="var(--rail)" stroke-width="1.3"/>
      <path d="M44 -5 L50 0 L44 5" fill="none" stroke="var(--ink)" stroke-width="1"/>
      <g fill="var(--ink)"><circle cx="63.5" cy="0" r="2.7"/><circle cx="104" cy="0" r="2.7"/><circle cx="223" cy="0" r="2.7"/></g>
      <g fill="#fff" stroke="var(--ink)" stroke-width="1"><circle cx="163" r="5"/><circle cx="262" r="5"/><circle cx="283.5" r="5"/></g>
      <circle cx="123.5" r="5" fill="#fff" stroke="var(--accent)" stroke-width="1"/>
      <g fill="var(--ink)"><circle cx="163" r="2.3"/><circle cx="262" r="2.3"/><circle cx="283.5" r="2.3"/></g>
      <circle cx="123.5" r="2.3" fill="var(--accent)"/>
      <text class="m" x="62.5" y="13">JAN</text><text class="m" x="104" y="13">MAR</text><text class="m" x="123.5" y="13">APR</text><text class="m" x="162" y="13">JUN</text><text class="m" x="223" y="13">SEP</text><text class="m" x="262" y="13">NOV</text><text class="m" x="283" y="13">DEZ</text>
    </g>
  </svg>
  <div class="topic-rule" style="top:140px"></div>
  <h3 class="topic-title" style="top:145px">Kick-off</h3>
  <h2 class="slide-title" style="top:225px;left:20px">Roadmap</h2>
  <div class="slide-year" style="top:228px">2021</div>
  <div class="brand-mark"></div>
</section>

</body>
</html>
```